KESTIVA GROUP OF CLINICS

We need a medical & lab report file. The design should be healthcare related. Our current file design has been used for almost 10 years. We need something more fresh & up-to-date. We have attached the current file design.

```html
<!DOCTYPE html>
<html lang="en">
<head>
<meta charset="utf-8">
<title>Kestiva Group of Clinics – Medical Report File</title>
<link href="https://fonts.googleapis.com/css2?family=Montserrat:wght@400;500;600;700;800&display=swap" rel="stylesheet">
<style>
  :root{
    --navy:#1f2a8a;
    --panel:#20309a;
    --panel-dark:#1a2580;
    --sky:#2b93e4;
    --sky-light:#3aa6f0;
    --white:#ffffff;
    --paper:#ffffff;
    --ghost:#e6e6e6;
    --bg:#ffffff;
  }
  *{margin:0;padding:0;box-sizing:border-box}
  html,body{width:1200px;height:3300px;overflow:hidden;background:var(--bg)}
  body{font-family:'Montserrat',sans-serif;position:relative}
  .spread{
    position:absolute;left:100px;top:1296px;width:1000px;height:708px;
    display:flex;box-shadow:0 8px 30px rgba(0,0,0,.18);
  }
  .back-cover{
    width:500px;height:100%;position:relative;overflow:hidden;
    background:linear-gradient(160deg,var(--panel) 0%,var(--panel-dark) 100%);
    color:var(--white);text-align:center;
  }
  .back-cover .pattern{
    position:absolute;inset:0;
    background:radial-gradient(circle at 25% 12%,rgba(255,255,255,.07),transparent 45%),
               radial-gradient(circle at 80% 85%,rgba(255,255,255,.05),transparent 40%);
  }
  .group-title{
    position:relative;margin-top:152px;font-size:21px;font-weight:600;letter-spacing:-.2px;
  }
  .clinic-list{position:relative;list-style:none;margin-top:18px}
  .clinic{margin-bottom:17px}
  .clinic-name{color:var(--sky-light);font-size:13px;font-weight:600;margin-bottom:5px}
  .clinic-address{font-size:8px;font-weight:400;line-height:1.5;display:flex;justify-content:center;gap:4px}
  .clinic-contacts{font-size:7.5px;display:flex;justify-content:center;gap:16px;margin-top:4px}
  .clinic-contacts span,.clinic-address span{display:inline-flex;align-items:center;gap:4px}
  .icon{width:9px;height:9px;fill:var(--sky-light);flex:none}

  .front-cover{
    width:500px;height:100%;background:var(--paper);position:relative;text-align:center;color:var(--navy);
  }
  .brand{
    position:absolute;top:88px;left:0;right:0;display:flex;justify-content:center;align-items:center;gap:10px;
  }
  .brand-dot{width:22px;height:22px;border-radius:50%;background:var(--sky)}
  .brand-name{font-size:26px;font-weight:700;color:var(--navy);letter-spacing:.5px}
  .tagline{position:absolute;top:196px;left:0;right:0}
  .tagline .group{font-size:13px;font-weight:600}
  .tagline .partner{font-size:18.5px;font-weight:700;margin-top:4px}
  .watermark{
    position:absolute;left:40px;top:240px;width:420px;height:330px;
    background:radial-gradient(ellipse at center,#ececec 0%,#f3f3f3 55%,rgba(255,255,255,0) 75%);
  }
  .report-title{position:absolute;top:588px;left:0;right:0;font-size:43px;font-weight:800;letter-spacing:-1px}
  .report-title .word-medical{color:var(--navy)}
  .report-title .word-report{color:var(--sky)}
  .report-sub{position:absolute;top:644px;left:0;right:0;font-size:14.5px;font-weight:600;letter-spacing:2.6px}
</style>
</head>
<body>
<svg width="0" height="0" style="position:absolute">
  <defs>
    <symbol id="i-pin" viewBox="0 0 24 24"><path d="M12 2a7 7 0 0 0-7 7c0 5 7 13 7 13s7-8 7-13a7 7 0 0 0-7-7zm0 9.5A2.5 2.5 0 1 1 12 6.5a2.5 2.5 0 0 1 0 5z"/></symbol>
    <symbol id="i-phone" viewBox="0 0 24 24"><path d="M6.6 10.8a15 15 0 0 0 6.6 6.6l2.2-2.2a1 1 0 0 1 1-.25 11.4 11.4 0 0 0 3.6.6 1 1 0 0 1 1 1V20a1 1 0 0 1-1 1A17 17 0 0 1 3 4a1 1 0 0 1 1-1h3.5a1 1 0 0 1 1 1c0 1.25.2 2.45.6 3.6a1 1 0 0 1-.25 1z"/></symbol>
    <symbol id="i-fax" viewBox="0 0 24 24"><path d="M6 2h9l3 3v5H6zM3 11h18v9H3zm3 3v2h4v-2zm8 0v2h4v-2z"/></symbol>
    <symbol id="i-mail" viewBox="0 0 24 24"><path d="M3 5h18v14H3zm2 2v.5l7 5 7-5V7z"/></symbol>
  </defs>
</svg>

<main class="spread">
  <section class="back-cover">
    <div class="pattern" role="img" aria-label="Faint decorative pattern on the blue panel"></div>
    <h2 class="group-title">KESTIVA GROUP OF CLINICS</h2>
    <ul class="clinic-list">
      <li class="clinic">
        <h3 class="clinic-name">PUSAT PERUBATAN KESTIVA</h3>
        <p class="clinic-address"><svg class="icon"><use href="#i-pin"/></svg>Level 12, Wisma Arunika, No 8 Jalan Seri Damai, 50450 Kuala Lumpur</p>
        <p class="clinic-contacts"><span><svg class="icon"><use href="#i-phone"/></svg>+603 2100 4410</span><span><svg class="icon"><use href="#i-fax"/></svg>+603 2100 4412</span><span><svg class="icon"><use href="#i-mail"/></svg>info@kestivamedical.com</span></p>
      </li>
      <li class="clinic">
        <h3 class="clinic-name">KLINIK KESTIVA (BUKIT JELUTONG)</h3>
        <p class="clinic-address"><svg class="icon"><use href="#i-pin"/></svg>No. 22, Jalan Pelangi U8/4, Bukit Jelutong, 40150 Shah Alam, Selangor Darul Ehsan</p>
        <p class="clinic-contacts"><span><svg class="icon"><use href="#i-phone"/></svg>+603 7810 2201</span><span><svg class="icon"><use href="#i-fax"/></svg>+603 7810 2202</span><span><svg class="icon"><use href="#i-mail"/></svg>jelutong@kestivamedical.com</span></p>
      </li>
      <li class="clinic">
        <h3 class="clinic-name">KLINIK KESTIVA (BAYAN LEPAS)</h3>
        <p class="clinic-address"><svg class="icon"><use href="#i-pin"/></svg>Lot 2-1-5, Lintang Cempaka 3, Taman Cempaka, 11900 Bayan Lepas, Penang</p>
        <p class="clinic-contacts"><span><svg class="icon"><use href="#i-phone"/></svg>604-610 3321</span><span><svg class="icon"><use href="#i-fax"/></svg>+604-610 3322</span><span><svg class="icon"><use href="#i-mail"/></svg>bayanlepas@kestivamedical.com</span></p>
      </li>
      <li class="clinic">
        <h3 class="clinic-name">KLINIK KESTIVA (SENDAYAN)</h3>
        <p class="clinic-address"><svg class="icon"><use href="#i-pin"/></svg><span>No. 45, Jalan Niaga Sendayan 2/4, Pusat Niaga Sendayan,<br>71950 Bandar Sri Sendayan, Negeri Sembilan</span></p>
        <p class="clinic-contacts"><span><svg class="icon"><use href="#i-phone"/></svg>+606-790 4410</span><span><svg class="icon"><use href="#i-fax"/></svg>+606-790 4412</span><span><svg class="icon"><use href="#i-mail"/></svg>sendayan@kestivamedical.com</span></p>
      </li>
      <li class="clinic">
        <h3 class="clinic-name">KESTIVA MEDICAL CLINIC (KLIA)</h3>
        <p class="clinic-address"><svg class="icon"><use href="#i-pin"/></svg>Unit A12, Arrival Hall, Main Terminal, 64000 Sepang, Selangor Darul Ehsan</p>
        <p class="clinic-contacts"><span><svg class="icon"><use href="#i-phone"/></svg>+603-8770 1180</span><span><svg class="icon"><use href="#i-fax"/></svg>+603-8770 1181</span><span><svg class="icon"><use href="#i-mail"/></svg>klia@kestivamedical.com</span></p>
      </li>
      <li class="clinic">
        <h3 class="clinic-name">KESTIVA MEDICAL CLINIC (KLIA2)</h3>
        <p class="clinic-address"><svg class="icon"><use href="#i-pin"/></svg>Unit L2-08, Landside Arrival Level, 64000 Sepang, Selangor Darul Ehsan</p>
        <p class="clinic-contacts"><span><svg class="icon"><use href="#i-phone"/></svg>+603-8770 2290</span><span><svg class="icon"><use href="#i-fax"/></svg>+603-8770 2291</span><span><svg class="icon"><use href="#i-mail"/></svg>klia2@kestivamedical.com</span></p>
      </li>
      <li class="clinic">
        <h3 class="clinic-name">KESTIVA MEDICAL CLINIC (PIA)</h3>
        <p class="clinic-address"><svg class="icon"><use href="#i-pin"/></svg>Unit G-14, Level 1, Passenger Terminal, 11900 Bayan Lepas, Penang</p>
        <p class="clinic-contacts"><span><svg class="icon"><use href="#i-phone"/></svg>+604 610 5510</span><span><svg class="icon"><use href="#i-fax"/></svg>+604 610 5511</span><span><svg class="icon"><use href="#i-mail"/></svg>pia@kestivamedical.com</span></p>
      </li>
    </ul>
  </section>

  <section class="front-cover">
    <div class="brand"><span class="brand-dot"></span><span class="brand-name">KESTIVA</span></div>
    <div class="tagline">
      <p class="group">KESTIVA GROUP</p>
      <p class="partner">YOUR HEALTHCARE PARTNER!</p>
    </div>
    <div class="watermark" role="img" aria-label="Large faint brand watermark area"></div>
    <h1 class="report-title"><span class="word-medical">MEDICAL</span> <span class="word-report">REPORT</span></h1>
    <p class="report-sub">PRIVATE &amp; CONFIDENTIAL</p>
  </section>
</main>
</body>
</html>
```